Handout for attendees of educational seminar

I provide educational workshops on how to give technical presentations at conferences to scientists and engineers. My company is called Craft Talk Studio (www.CraftTalkStudio.example). I would like a double sided, half page size flyer that can be used as a handout for attendees of my workshops. On one side of the flyer, they will get top tips for creating their next presentation. On the other side, they will get my photo, bio, and contact information. I have uploaded a draft of a full page design I made myself. I'd like the copy of the tips to remain the same, but everything else is flexible.

Target Market(s)

scientists, engineers, technical professionals

Font styles to use
Serif
Sans Serif

Requirements
Must have
• my photo (I've provided two options to choose from depending on colors...photo on side 2 only), my logo, flyer needs to be half page in size (5.5" x 8.5"), needs to be double sided, One side has the "tips" and the other side has my personal details (see attached page for copy).
Nice to have
• I like the use of icons on the "tips" side of the flyer.

```html
<!DOCTYPE html>
<html lang="en">
<head>
<meta charset="utf-8">
<title>Craft Talk Studio – Workshop Handout</title>
<link href="https://fonts.googleapis.com/css2?family=Maven+Pro:wght@400;500;600;700&family=Hind:wght@300;400&display=swap" rel="stylesheet">
<style>
  :root{
    --stage:#6b6b6b;
    --paper:#ffffff;
    --green:#2e9a3a;
    --blue:#1c9be6;
    --charcoal:#2f2f2f;
    --ink:#1a1a1a;
    --body:#2a2a2a;
  }
  *{box-sizing:border-box;margin:0;padding:0}
  html,body{width:1200px;height:1200px;overflow:hidden}
  body{background:var(--stage);position:relative;font-family:"Hind",sans-serif;color:var(--ink)}
  .sheet{position:absolute;background:var(--paper);overflow:hidden}
  .sheet--tips{left:28px;top:191px;width:558px;height:863px}
  .sheet--bio{left:614px;top:193px;width:556px;height:857px}
  .hero{position:absolute;left:0;top:0}
  .brand{position:absolute;left:368px;top:18px;width:170px;text-align:center}
  .brand__dot{display:block;width:60px;height:60px;border-radius:50%;background:#4a4a4a;margin:0 auto 10px}
  .brand__name{font-family:"Maven Pro",sans-serif;font-size:20px;color:var(--green);font-weight:400;line-height:1}
  .brand__tag{font-family:"Maven Pro",sans-serif;font-size:7px;letter-spacing:2.4px;color:var(--green);margin-top:3px}
  .title{position:absolute;left:42px;top:423px;font-family:"Maven Pro",sans-serif;font-weight:500;font-size:50px;color:var(--green);line-height:1}
  .subtitle{position:absolute;left:43px;top:477px;font-family:"Maven Pro",sans-serif;font-size:27px;color:var(--blue);line-height:1}
  .slogan{position:absolute;left:43px;top:507px;font-family:"Maven Pro",sans-serif;font-size:18px;color:var(--ink)}
  .tip{position:absolute;left:0;width:558px}
  .tip__icon{position:absolute;left:44px;top:2px}
  .tip__head{position:absolute;left:121px;top:0;font-family:"Maven Pro",sans-serif;font-size:16px;color:var(--green)}
  .tip__text{position:absolute;left:121px;top:22px;width:400px;font-size:10.6px;line-height:13.6px;color:var(--body)}
  .footer{position:absolute;left:0;bottom:0;width:100%;background:var(--blue);color:#fff;font-family:"Maven Pro",sans-serif}
  .sheet--tips .footer{height:77px}
  .contact{position:absolute;left:52px;font-size:17px;display:flex;align-items:center;gap:18px}
  .contact svg{flex:none}
  .divider{position:absolute;top:12px;width:1px;height:53px;background:rgba(255,255,255,.8)}
  .follow{position:absolute;font-size:23px}
  .socials{position:absolute;display:flex;gap:22px}
  .socials span{display:block;border-radius:50%;background:#fff}
  .photo{position:absolute;left:0;top:0}
  .bio{position:absolute;left:45px;top:350px;width:468px;font-size:14.6px;line-height:18.8px;color:var(--body);text-align:justify}
  .bio p{margin-bottom:6px}
  .quote{position:absolute;font-family:"Maven Pro",sans-serif;font-weight:700;font-size:40px;color:var(--green);line-height:1}
  .meet{position:absolute;right:42px;top:718px;font-family:"Maven Pro",sans-serif;font-size:26px;color:var(--green);border-bottom:2px solid var(--green);padding-bottom:2px;line-height:1.1}
  .meet-tag{position:absolute;right:42px;top:763px;font-family:"Maven Pro",sans-serif;font-size:15px;color:var(--ink)}
  .sheet--bio .footer{height:67px}
  .col{position:absolute;top:10px;text-align:center;font-size:12.5px}
  .col svg{display:block;margin:0 auto 8px}
</style>
</head>
<body>

<section class="sheet sheet--tips" aria-label="Quick tips side">
  <svg class="hero" width="558" height="460" viewBox="0 0 558 460">
    <defs>
      <linearGradient id="stageGlow" x1="0" y1="0" x2="1" y2="1">
        <stop offset="0" stop-color="#1c1440"/>
        <stop offset="0.45" stop-color="#5a1f7a"/>
        <stop offset="0.8" stop-color="#a3243a"/>
        <stop offset="1" stop-color="#7a1020"/>
      </linearGradient>
      <linearGradient id="portraitTone" x1="0" y1="0" x2="0" y2="1">
        <stop offset="0" stop-color="#b49a76"/>
        <stop offset="1" stop-color="#4a3d35"/>
      </linearGradient>
    </defs>
    <path role="img" aria-label="Photo of the presenter speaking on a conference stage" d="M0 0H558V180C470 250 330 320 200 345C100 365 30 380 0 420Z" fill="url(#stageGlow)"/>
    <path d="M0 420C30 380 100 365 200 345C330 320 470 250 558 180V205C470 280 340 335 210 360C110 380 30 400 0 440Z" fill="var(--green)"/>
    <path d="M0 440C30 400 110 380 210 360C340 335 470 280 558 205V240C470 320 350 365 220 385C110 402 30 420 0 455Z" fill="var(--blue)"/>
    <path d="M0 455C30 420 110 402 220 385C350 365 470 320 558 240V460H0Z" fill="#fff"/>
    <ellipse cx="452" cy="50" rx="130" ry="90" fill="#fff" stroke="var(--green)" stroke-width="3"/>
    <circle cx="358" cy="313" r="104" fill="var(--blue)"/>
    <circle role="img" aria-label="Close-up portrait photo of the presenter" cx="358" cy="313" r="99" fill="url(#portraitTone)"/>
  </svg>

  <div class="brand">
    <span class="brand__dot"></span>
    <div class="brand__name">Dana Whitfield</div>
    <div class="brand__tag">Craft Talk Studio</div>
  </div>

  <h1 class="title">Craft Talk Studio</h1>
  <div class="subtitle">QUICK TIPS</div>
  <div class="slogan">Science not communicated is science not done!</div>

  <div class="tip" style="top:545px">
    <svg class="tip__icon" width="50" height="50" viewBox="0 0 50 50">
      <circle cx="25" cy="25" r="23" fill="var(--green)"/>
      <path d="M14 25l8 8 14-16" fill="none" stroke="#fff" stroke-width="4" stroke-linecap="round" stroke-linejoin="round"/>
    </svg>
    <div class="tip__head">Be Audience Centered</div>
    <p class="tip__text">Your ability to be successful as a speaker depends upon your ability to make your audience successful. TIP: Return to "Points of Common Ground" throughout the talk that answer the question "So what?" about the scientific info. Be an interpreter!</p>
  </div>

  <div class="tip" style="top:627px">
    <svg class="tip__icon" width="50" height="50" viewBox="0 0 50 50">
      <circle cx="25" cy="25" r="23" fill="var(--blue)"/>
      <path d="M25 12v24M15 27l10 10 10-10" fill="none" stroke="#fff" stroke-width="4" stroke-linecap="round" stroke-linejoin="round"/>
    </svg>
    <div class="tip__head">Filter &amp; Focus</div>
    <p class="tip__text">When you try to share everything, you share nothing. TIP: Start your planning with the "view" you want your audience to have at the end of the talk. Then ask yourself "What would they need to know in order to get there?"</p>
  </div>

  <div class="tip" style="top:707px">
    <svg class="tip__icon" width="50" height="50" viewBox="0 0 50 50">
      <circle cx="25" cy="25" r="23" fill="var(--charcoal)"/>
      <path d="M13 25h22M27 16l9 9-9 9" fill="none" stroke="#fff" stroke-width="4" stroke-linecap="round" stroke-linejoin="round"/>
    </svg>
    <div class="tip__head">Show Your Science</div>
    <p class="tip__text">Your slides should do something for you that your words cannot. This means make your slides VISUAL not VERBAL. TIP: NO BULLET POINTS (seriously!). Have a brief take-away messages supported by visual evidence.</p>
  </div>

  <footer class="footer">
    <div class="contact" style="top:10px;left:52px">
      <svg width="18" height="18" viewBox="0 0 18 18" fill="none" stroke="#fff" stroke-width="1.4"><circle cx="9" cy="9" r="8"/><ellipse cx="9" cy="9" rx="3.5" ry="8"/><path d="M1 9h16M2.5 5h13M2.5 13h13"/></svg>
      <span>www.CraftTalkStudio.example</span>
    </div>
    <div class="contact" style="top:44px;left:52px">
      <svg width="18" height="18" viewBox="0 0 18 18" fill="none" stroke="#fff" stroke-width="1.4"><circle cx="9" cy="9" r="8"/><rect x="4.5" y="5.5" width="9" height="7"/><path d="M4.5 5.5L9 9.5l4.5-4"/></svg>
      <span>dana@crafttalkstudio.example</span>
    </div>
    <div class="divider" style="left:373px"></div>
    <div class="follow" style="left:402px;top:9px">Fllow Us:</div>
    <div class="socials" style="left:398px;top:45px">
      <span style="width:20px;height:20px"></span>
      <span style="width:20px;height:20px"></span>
      <span style="width:20px;height:20px"></span>
    </div>
  </footer>
</section>

<section class="sheet sheet--bio" aria-label="About side">
  <svg class="photo" width="556" height="340" viewBox="0 0 556 340">
    <defs>
      <linearGradient id="headshotTone" x1="0" y1="0" x2="1" y2="1">
        <stop offset="0" stop-color="#d9d2c6"/>
        <stop offset="0.5" stop-color="#b58f6e"/>
        <stop offset="1" stop-color="#6f8a5c"/>
      </linearGradient>
    </defs>
    <path role="img" aria-label="Smiling headshot photo of the workshop leader" d="M0 0H556V265C430 330 250 340 130 320C70 310 30 300 0 290Z" fill="url(#headshotTone)"/>
    <path d="M0 290C30 300 70 310 130 320C250 340 430 330 556 265V272C430 340 250 350 120 337C60 330 25 320 0 308Z" fill="var(--blue)"/>
  </svg>

  <span class="quote" style="left:18px;top:345px">&ldquo;</span>
  <div class="bio">
    <p>Dana Whitfield is on a mission: to transform how scientists, engineers, and technical professionals present their work. That's because she believes that even the best technical ideas are destined to remain undiscovered unless presented in a clear and compelling way that sparks innovation and drives adoption.</p>
    <p>For a decade, she's traveled around the world to work with Top 100 corporations, institutions and universities, teaching the proven strategies she's mastered through her consulting work and during her time as a faculty member Northfield State University.</p>
    <p>Dana is internationally known for her popular Main Stage talk entitled "Speak Clearly to Me" which has over 2 million views (and counting!).</p>
    <p>Teams that work with Dana get the practical skills and natural confidence they need to immediately shift their "information dump"-style presentations into ones that are meaningful, engaging, and inspire people to take action.</p>
    <p>Dana provides on-site group workshops and coaching, conference sessions and keynotes, and 1:1 consultation.</p>
  </div>
  <span class="quote" style="left:342px;top:700px">&rdquo;</span>

  <div class="meet">Meet Dana</div>
  <div class="meet-tag">Science not communicated is science not done</div>

  <footer class="footer">
    <div class="col" style="left:18px;width:190px">
      <svg width="22" height="22" viewBox="0 0 18 18" fill="none" stroke="#fff" stroke-width="1.3"><circle cx="9" cy="9" r="8"/><ellipse cx="9" cy="9" rx="3.5" ry="8"/><path d="M1 9h16M2.5 5h13M2.5 13h13"/></svg>
      www.CraftTalkStudio.example
    </div>
    <div class="divider" style="left:217px;top:8px"></div>
    <div class="col" style="left:225px;width:212px">
      <svg width="22" height="22" viewBox="0 0 18 18" fill="none" stroke="#fff" stroke-width="1.3"><circle cx="9" cy="9" r="8"/><rect x="4.5" y="5.5" width="9" height="7"/><path d="M4.5 5.5L9 9.5l4.5-4"/></svg>
      dana@crafttalkstudio.example
    </div>
    <div class="divider" style="left:437px;top:8px"></div>
    <div class="follow" style="left:456px;top:10px;font-size:13px">Fllow Us:</div>
    <div class="socials" style="left:452px;top:36px;gap:8px">
      <span style="width:15px;height:15px"></span>
      <span style="width:15px;height:15px"></span>
      <span style="width:15px;height:15px"></span>
    </div>
  </footer>
</section>

</body>
</html>
```